Pediatric Dental Practice needs a postcard for direct mail advertising

We are looking for a creative and professional double-sided postcard design for a direct mail marketing campaign. Our goal is to attract new families to our pediatric dental practice by conveying a sense of warmth, modern care, and clinical excellence. The design should feel "boutique" and high-end yet remain fun and approachable for parents and children.

```html
<!DOCTYPE html>
<html lang="en">
<head>
<meta charset="utf-8">
<title>Maple Grove Pediatric Dentistry – New Patient Postcard</title>
<link rel="stylesheet" href="https://fonts.googleapis.com/css2?family=Montserrat:wght@400;500;600;700;800&family=Montserrat+Alternates:wght@500;700;800&family=Great+Vibes&display=swap">
<style>
  :root{
    --green:#2f9e58;
    --green-deep:#1f8a47;
    --green-soft:#cfe9d6;
    --green-mist:#e8f5ec;
    --ink:#2b2f2c;
    --ink-soft:#3d423f;
    --paper:#ffffff;
    --stage:#e7e8e8;
  }
  *{box-sizing:border-box;margin:0;padding:0}
  html,body{width:1117px;height:1200px;overflow:hidden;background:var(--stage)}
  body{font-family:"Montserrat",sans-serif;color:var(--ink);position:relative}
  .postcard{position:absolute;left:138px;width:840px;height:560px;background:var(--paper);overflow:hidden;box-shadow:0 6px 18px rgba(0,0,0,.12)}
  .postcard--front{top:30px}
  .postcard--back{top:610px}
  .abs{position:absolute}

  /* FRONT */
  .front-wash{left:0;top:0;width:840px;height:560px}
  .brand{left:37px;top:30px;width:250px;text-align:center}
  .brand__dot{width:56px;height:56px;border-radius:50%;background:var(--green-soft);margin:0 auto 12px}
  .brand__name{font-family:"Montserrat",sans-serif;font-weight:500;font-size:34px;color:var(--ink-soft);line-height:1}
  .brand__descriptor{font-size:11.5px;letter-spacing:3.2px;color:var(--ink-soft);margin-top:6px}
  .headline{left:34px;top:208px;font-family:"Montserrat Alternates",sans-serif;color:var(--green);line-height:1}
  .headline__small{font-weight:500;font-size:44px;display:block}
  .headline__big{font-weight:800;font-size:64px;display:block;margin-top:4px}
  .intro{left:36px;top:368px;border-left:2px solid var(--ink-soft);padding-left:10px;font-size:20px;line-height:23px;color:var(--ink);font-weight:500}
  .tagline{left:37px;top:502px;font-size:14px;line-height:17px;color:var(--green);font-weight:500}
  .photo{border-radius:50%;border:4px solid var(--green-soft)}
  .photo--main{left:330px;top:38px;width:476px;height:288px;background:radial-gradient(ellipse at 55% 50%,#d9cfe6 0%,#b8c7d8 45%,#6f8fb8 100%)}
  .photo--girl{left:417px;top:265px;width:124px;height:124px;background:radial-gradient(circle,#d8c2b4,#8d97a7)}
  .photo--exam{left:575px;top:273px;width:118px;height:118px;background:radial-gradient(circle,#a58c7a,#3f3b3d)}
  .photo--chair{left:703px;top:226px;width:98px;height:98px;background:radial-gradient(circle,#f0c9b0,#c9414d)}
  .welcome{left:500px;top:418px;width:320px;height:110px}
  .welcome__now{left:165px;top:0;font-size:30px;font-weight:500;color:var(--ink)}
  .welcome__script{left:0;top:12px;font-family:"Great Vibes",cursive;font-size:82px;color:var(--green-deep);line-height:1}
  .welcome__sub{left:18px;top:70px;font-size:32px;font-weight:500;color:var(--ink)}
  .corner{right:0;bottom:0;width:56px;height:66px}

  /* BACK */
  .back-band{left:0;top:0;width:290px;height:10px;background:var(--green-soft)}
  .intro-title{left:36px;top:34px;font-family:"Montserrat Alternates",sans-serif;color:var(--green);font-size:28px;line-height:29px}
  .intro-title strong{font-weight:800}
  .intro-copy{left:36px;top:140px;width:410px;font-size:13.5px;line-height:17px;color:var(--ink)}
  .reasons{left:0;top:234px;width:447px;height:212px;border-radius:0 20px 20px 0;border-top:2px solid var(--green-soft);background:linear-gradient(90deg,#fff 0%,#fff 45%,var(--green-mist) 70%,#9fd6ae 100%);padding:14px 0 0 36px}
  .reasons__title{font-family:"Montserrat Alternates",sans-serif;font-size:25px;color:var(--green);font-weight:500;margin-bottom:14px}
  .reasons__title strong{font-weight:800}
  .reasons__list{list-style:none}
  .reasons__item{display:flex;align-items:center;gap:8px;font-size:15px;font-weight:600;height:28px}
  .reasons__icon{width:19px;height:19px;flex:none}
  .contact{left:36px;top:464px}
  .contact__row{display:flex;align-items:center;gap:12px}
  .contact__phone{font-size:29px;font-weight:700}
  .contact__email{font-size:17px;margin-top:6px}
  .contact__icon{width:28px;height:28px;flex:none}
  .stamp{left:671px;top:34px;width:134px;height:160px;border:1px solid var(--ink)}
  .address-line{left:484px;width:321px;height:1px;background:var(--ink-soft)}
</style>
</head>
<body>

<section class="postcard postcard--front" aria-label="Postcard front">
  <svg class="abs front-wash" viewBox="0 0 840 560" aria-hidden="true">
    <defs>
      <linearGradient id="washGrad" x1="0" y1="0" x2="1" y2="0.4">
        <stop offset="0" stop-color="#c9e7d1"/>
        <stop offset="0.7" stop-color="#eef8f1"/>
        <stop offset="1" stop-color="#ffffff"/>
      </linearGradient>
    </defs>
    <path d="M0 0 H570 C470 60 420 180 440 300 C330 390 170 420 0 430 Z" fill="url(#washGrad)"/>
    <path d="M0 450 C170 450 330 410 440 330" fill="none" stroke="#cfe9d6" stroke-width="5" stroke-linecap="round"/>
    <circle cx="700" cy="35" r="7" fill="#cfe9d6"/>
  </svg>

  <div class="abs brand">
    <div class="brand__dot"></div>
    <div class="brand__name">maple grove</div>
    <div class="brand__descriptor">PEDIATRIC DENTISTRY</div>
  </div>

  <h1 class="abs headline">
    <span class="headline__small">Little Smiles.</span>
    <span class="headline__big">Big Care.</span>
  </h1>

  <p class="abs intro">Gentle, modern dentistry<br>designed just for children.</p>

  <p class="abs tagline">Creating confident smiles in a calm, friendly environment<br>— where kids feel safe and parents feel reassured.</p>

  <div class="abs photo photo--main" role="img" aria-label="Photo of a dentist examining a smiling young girl in a dental chair"></div>
  <div class="abs photo photo--girl" role="img" aria-label="Photo of a young girl touching her cheek"></div>
  <div class="abs photo photo--exam" role="img" aria-label="Photo of a child having a dental check-up"></div>
  <div class="abs photo photo--chair" role="img" aria-label="Photo of a smiling red-haired child in a dental chair"></div>

  <div class="abs welcome">
    <span class="abs welcome__now">Now</span>
    <span class="abs welcome__script">Welcoming</span>
    <span class="abs welcome__sub">New Patients</span>
  </div>

  <svg class="abs corner" viewBox="0 0 56 66" aria-hidden="true">
    <path d="M56 0 C20 6 4 34 0 66 H56 Z" fill="#cfe9d6"/>
    <path d="M56 12 C26 18 12 40 8 66 H56 Z" fill="#1f8a47"/>
  </svg>
</section>

<section class="postcard postcard--back" aria-label="Postcard back">
  <div class="abs back-band"></div>
  <svg class="abs" style="left:310px;top:28px" width="20" height="20" aria-hidden="true"><circle cx="10" cy="10" r="7" fill="#cfe9d6"/></svg>

  <h2 class="abs intro-title">A Better<br><strong>Dental Experience</strong><br>for Your Child</h2>

  <p class="abs intro-copy">At Maple Grove Pediatric Dentistry, we believe every child deserves a positive start to their dental journey.<br>Our boutique-style practice combines advanced technology with a warm, personalised approach — helping children feel relaxed, comfortable, and cared for at every visit.</p>

  <div class="abs reasons">
    <h3 class="reasons__title">Why Parents <strong>Choose Us:</strong></h3>
    <ul class="reasons__list">
      <li class="reasons__item"><svg class="reasons__icon" viewBox="0 0 20 20" aria-hidden="true"><circle cx="10" cy="10" r="8" fill="none" stroke="#2f9e58" stroke-width="1.5"/><path d="M6 10.5l3 3 5-6" fill="none" stroke="#2f9e58" stroke-width="1.5"/></svg>Gentle, child-focused care</li>
      <li class="reasons__item"><svg class="reasons__icon" viewBox="0 0 20 20" aria-hidden="true"><circle cx="10" cy="10" r="8" fill="none" stroke="#2f9e58" stroke-width="1.5"/><path d="M6 10.5l3 3 5-6" fill="none" stroke="#2f9e58" stroke-width="1.5"/></svg>Calm, modern, boutique environment</li>
      <li class="reasons__item"><svg class="reasons__icon" viewBox="0 0 20 20" aria-hidden="true"><circle cx="10" cy="10" r="8" fill="none" stroke="#2f9e58" stroke-width="1.5"/><path d="M6 10.5l3 3 5-6" fill="none" stroke="#2f9e58" stroke-width="1.5"/></svg>Friendly and experienced team</li>
      <li class="reasons__item"><svg class="reasons__icon" viewBox="0 0 20 20" aria-hidden="true"><circle cx="10" cy="10" r="8" fill="none" stroke="#2f9e58" stroke-width="1.5"/><path d="M6 10.5l3 3 5-6" fill="none" stroke="#2f9e58" stroke-width="1.5"/></svg>Preventive &amp; comprehensive pediatric dentistry</li>
      <li class="reasons__item"><svg class="reasons__icon" viewBox="0 0 20 20" aria-hidden="true"><circle cx="10" cy="10" r="8" fill="none" stroke="#2f9e58" stroke-width="1.5"/><path d="M6 10.5l3 3 5-6" fill="none" stroke="#2f9e58" stroke-width="1.5"/></svg>Designed to make kids feel safe and confident</li>
    </ul>
  </div>

  <div class="abs contact">
    <div class="contact__row contact__phone">
      <svg class="contact__icon" viewBox="0 0 24 24" aria-hidden="true"><path d="M6.6 3.5l2.6 3.3-1.6 2.2c1.2 2.6 3 4.4 5.5 5.5l2.2-1.6 3.3 2.6-1.4 3.2C9.8 19 5 14.2 3.4 4.9z" fill="none" stroke="#2f9e58" stroke-width="2" stroke-linejoin="round"/></svg>
      (555) 014-2870
    </div>
    <div class="contact__row contact__email">
      <svg class="contact__icon" viewBox="0 0 24 24" aria-hidden="true"><circle cx="12" cy="12" r="9" fill="none" stroke="#2f9e58" stroke-width="1.8"/><ellipse cx="12" cy="12" rx="4" ry="9" fill="none" stroke="#2f9e58" stroke-width="1.5"/><path d="M3 12h18M5 7h14M5 17h14" stroke="#2f9e58" stroke-width="1.3"/></svg>
      hello@maplegrovekids.com
    </div>
  </div>

  <div class="abs stamp" aria-label="Stamp area"></div>
  <div class="abs address-line" style="top:279px"></div>
  <div class="abs address-line" style="top:336px"></div>
  <div class="abs address-line" style="top:393px"></div>
  <div class="abs address-line" style="top:449px"></div>

  <svg class="abs corner" viewBox="0 0 56 66" aria-hidden="true">
    <path d="M56 0 C20 6 4 34 0 66 H56 Z" fill="#cfe9d6"/>
    <path d="M56 12 C26 18 12 40 8 66 H56 Z" fill="#1f8a47"/>
  </svg>
</section>

</body>
</html>
```